Clever & creative business card needed for a pediatric dentist.

We need a business card for a pediatric dentist that is building a brand-new pediatric dental practice. He is funny, outgoing, and sociable, and he hopes to give his business card to dentists and pediatricians so that he can give them information of where to refer infants, children, and teenagers that need high quality and attainable dental care.

The name of the dental practice is Copper Fern Pediatric Dentistry. Logo design .png / .pdf/ .jpg are provided to aid in the design.

The dentist's last name is Tolvan (which sounds like "burger", as in "hamburger” or “cheeseburger"). Since it is pediatric practice, kudos will be given to designs that implement a little joke into the design - but hopefully in a small or hidden way (such as putting something like a cheeseburger on the back of the card, or hiding it an an abstract way).

Thank you!

Please make a design that incorporates colors. It should be fun! Not too serious. It does not have to follow the color scheme of the logos.

```html
<!DOCTYPE html>
<html lang="en">
<head>
<meta charset="utf-8">
<title>Copper Fern Pediatric Dentistry – Business Card</title>
<link rel="stylesheet" href="https://fonts.googleapis.com/css2?family=Montserrat:wght@400;500;600&display=swap">
<style>
  :root {
    --backdrop: #5b5b5d;
    --card-dark: #3a3a3c;
    --card-light: #ffffff;
    --ink: #2f2f31;
    --ink-soft: #3c3c3e;
    --green-deep: #2f9a57;
    --green-mid: #52b86f;
    --green-soft: #86cf93;
    --green-pale: #b9e3bd;
    --pattern-dark: #434345;
    --pattern-light: #f1f1f1;
  }
  * { box-sizing: border-box; margin: 0; padding: 0; }
  html, body { width: 1200px; height: 1095px; overflow: hidden; }
  body {
    background: var(--backdrop);
    font-family: "Montserrat", Arial, sans-serif;
    position: relative;
  }
  .card {
    position: absolute;
    width: 620px;
    height: 355px;
    border-radius: 16px;
    overflow: hidden;
    box-shadow: 0 18px 40px rgba(0,0,0,.35);
  }
  .card--front { left: 110px; top: 95px; background: var(--card-dark); }
  .card--back  { left: 470px; top: 620px; background: var(--card-light); }

  .card__pattern { position: absolute; inset: 0; }
  .card--front .card__pattern {
    background: radial-gradient(circle at 50% 45%, var(--pattern-dark), var(--card-dark) 75%);
  }
  .card--back .card__pattern {
    background: radial-gradient(circle at 55% 40%, var(--pattern-light), var(--card-light) 80%);
  }

  .brand {
    position: absolute;
    display: flex;
    align-items: center;
    gap: 14px;
  }
  .brand__dot {
    width: 34px; height: 34px; border-radius: 50%;
    background: var(--green-mid);
    flex: none;
  }
  .brand__name {
    font-weight: 600;
    font-size: 30px;
    line-height: 1.15;
    letter-spacing: .5px;
  }
  .card--front .brand { left: 150px; top: 135px; }
  .card--front .brand__name { color: #ffffff; }
  .card--back .brand { left: 40px; top: 130px; }
  .card--back .brand__name { color: var(--ink); font-size: 26px; }

  .divider {
    position: absolute;
    left: 300px; top: 62px;
    width: 2px; height: 190px;
    background: var(--ink-soft);
  }
  .divider::after {
    content: "";
    position: absolute;
    left: -1px; top: 40px;
    width: 4px; height: 110px;
    background: var(--green-deep);
  }

  .contact {
    position: absolute;
    left: 325px; top: 56px;
    color: var(--ink);
  }
  .contact__name {
    font-weight: 600;
    font-size: 27px;
    color: var(--green-deep);
    line-height: 1.1;
  }
  .contact__role { font-size: 14px; font-weight: 500; margin: 4px 0 10px; }
  .contact__line { font-size: 14px; line-height: 1.5; }
  .contact__list { list-style: none; margin-top: 10px; }
  .contact__list li {
    display: flex; align-items: center; gap: 8px;
    font-size: 14px; line-height: 1.6;
  }
  .contact__list svg { width: 13px; height: 13px; fill: var(--green-deep); flex: none; }

  .stripe {
    position: absolute;
    left: 0; right: 0; bottom: 0;
    height: 16px;
    display: flex;
    gap: 3px;
  }
  .stripe span { flex: 1; }
  .stripe span:nth-child(1) { background: var(--green-deep); }
  .stripe span:nth-child(2) { background: var(--green-mid); }
  .stripe span:nth-child(3) { background: var(--green-soft); }
  .stripe span:nth-child(4) { background: var(--green-pale); }
</style>
</head>
<body>

<section class="card card--front">
  <div class="card__pattern" role="img" aria-label="Faint repeating cheeseburger pattern"></div>
  <div class="brand">
    <span class="brand__dot"></span>
    <p class="brand__name">Copper Fern<br>Pediatric Dentistry</p>
  </div>
</section>

<section class="card card--back">
  <div class="card__pattern" role="img" aria-label="Faint repeating cheeseburger pattern"></div>
  <div class="brand">
    <span class="brand__dot"></span>
    <p class="brand__name">Copper Fern<br>Pediatric<br>Dentistry</p>
  </div>
  <div class="divider"></div>
  <div class="contact">
    <h1 class="contact__name">Marek Tolvan</h1>
    <p class="contact__role">Pediatric Dentist</p>
    <p class="contact__line">5120 Birch Road</p>
    <p class="contact__line">Alden, NE 68590</p>
    <ul class="contact__list">
      <li><svg viewBox="0 0 24 24"><path d="M6.6 10.8a15 15 0 0 0 6.6 6.6l2.2-2.2c.3-.3.7-.4 1-.2 1.1.4 2.3.6 3.6.6.6 0 1 .4 1 1V20c0 .6-.4 1-1 1A17 17 0 0 1 3 4c0-.6.4-1 1-1h3.5c.6 0 1 .4 1 1 0 1.3.2 2.5.6 3.6.1.3 0 .7-.2 1z"/></svg>+555-204-7316</li>
      <li><svg viewBox="0 0 24 24"><path d="M2 5h20v14H2z M3 6l9 7 9-7" stroke="#fff" stroke-width="1.5"/></svg>hello@copperfern.com</li>
      <li><svg viewBox="0 0 24 24"><circle cx="12" cy="12" r="10"/></svg>www.copperfern.com</li>
    </ul>
  </div>
  <div class="stripe"><span></span><span></span><span></span><span></span></div>
</section>

</body>
</html>
```